BuildLinkage.com Full Stationery Design

Business Card will have all info on it. Letterhead will not have name, title or mobile number. Keep general feeling very clean, using colors from the logo as accents.
Name:Dale Vanterpool
Title:President
Phone: 1-800-555-4926
Cell: 222-555-7312
email: dale@buildlinkage.com
website: www.buildlinkage.com
Address:
PO Box 874
Brockridge, NR
S0M2T7

Target Market(s)

Construction Business owners

Industry/Entity Type

Business

Contact Information for Business Card

Name:Dale Vanterpool
Title:President
Phone: 1-800-555-4926
Cell: 222-555-7312
Address:
PO Box 874
Brockridge, NR
S0M2T7

Font styles to use
Sans Serif

Requirements
Must have
• Clean look
Should not have
• Images or cartoon type characters or tools

```html
<!DOCTYPE html>
<html lang="en">
<head>
<meta charset="utf-8">
<title>BuildLinkage.com Business Card</title>
<link rel="stylesheet" href="https://fonts.googleapis.com/css2?family=Open+Sans:wght@400;600&display=swap">
<style>
  :root {
    --backdrop: #d6d6d8;
    --slate-dark: #4a5a6d;
    --slate-light: #6c7f8f;
    --slate-text: #4b5a6c;
    --orange: #f47b20;
    --red: #e8262d;
    --rule: #d2d2d2;
    --white: #ffffff;
    --ink: #3c3c3c;
  }
  * { box-sizing: border-box; margin: 0; padding: 0; }
  html, body {
    width: 1200px; height: 1200px; overflow: hidden;
    background: var(--backdrop);
    font-family: "Open Sans", Arial, sans-serif;
  }
  .sheet {
    width: 1200px; height: 1200px;
    display: flex; flex-direction: column; align-items: center; justify-content: center; gap: 36px;
  }
  .card {
    position: relative;
    width: 860px; height: 492px;
    overflow: hidden;
    box-shadow: 0 6px 18px rgba(0,0,0,0.18);
  }
  .card--back {
    background: linear-gradient(110deg, var(--slate-dark) 0%, var(--slate-light) 100%);
    display: flex; align-items: center; justify-content: center;
  }
  .brand { display: flex; align-items: center; gap: 22px; }
  .brand__mark { width: 64px; height: 64px; background: var(--orange); }
  .brand__divider { width: 2px; height: 84px; background: currentColor; opacity: 0.5; }
  .brand__name { font-weight: 600; font-size: 46px; letter-spacing: 0.5px; white-space: nowrap; }
  .card--back .brand { color: var(--white); }
  .card--front { background: var(--white); }
  .card--front .brand {
    position: absolute; left: 66px; top: 70px; color: var(--slate-text);
  }
  .card--front .brand__mark { width: 50px; height: 50px; }
  .card--front .brand__divider { height: 62px; background: var(--rule); opacity: 1; }
  .card--front .brand__name { font-size: 34px; }
  .person { position: absolute; right: 66px; top: 196px; text-align: right; }
  .person__name { font-size: 32px; color: var(--slate-text); font-weight: 400; white-space: nowrap; }
  .person__title { font-size: 17px; color: var(--orange); margin-top: -2px; }
  .divider-line {
    position: absolute; left: 150px; right: 66px; top: 292px;
    height: 1.5px; background: var(--rule);
  }
  .contacts {
    position: absolute; left: 150px; top: 310px;
    list-style: none; font-size: 19px; color: var(--ink); line-height: 30px;
  }
  .contacts li { display: flex; align-items: center; gap: 12px; white-space: nowrap; }
  .contacts svg { width: 16px; height: 16px; flex: none; }
  .address {
    position: absolute; right: 66px; top: 318px;
    text-align: right; font-size: 17px; color: var(--ink); line-height: 24px; white-space: nowrap;
  }
  .footer-band { position: absolute; left: 0; right: 0; bottom: 0; height: 46px; }
  .footer-band__slate {
    position: absolute; left: 0; top: 12px; bottom: 0; width: 64%;
    background: linear-gradient(90deg, var(--slate-dark), var(--slate-light));
  }
  .footer-band__accent {
    position: absolute; right: 0; top: 0; bottom: 0; left: 62%;
    background: linear-gradient(90deg, var(--red), var(--orange));
    clip-path: polygon(14px 0, 100% 0, 100% 100%, 0 100%);
    display: flex; align-items: center; justify-content: flex-end; padding-right: 40px;
    color: var(--white); font-size: 17px; white-space: nowrap;
  }
</style>
</head>
<body>
<main class="sheet">
  <section class="card card--back" aria-label="Business card back">
    <div class="brand">
      <div class="brand__mark"></div>
      <div class="brand__divider"></div>
      <div class="brand__name">BuildLinkage.com</div>
    </div>
  </section>

  <section class="card card--front" aria-label="Business card front">
    <div class="brand">
      <div class="brand__mark"></div>
      <div class="brand__divider"></div>
      <div class="brand__name">BuildLinkage.com</div>
    </div>

    <div class="person">
      <div class="person__name">Dale Vanterpool</div>
      <div class="person__title">President</div>
    </div>

    <div class="divider-line"></div>

    <ul class="contacts">
      <li>
        <svg viewBox="0 0 16 16"><path fill="#f47b20" d="M4 1c1 0 2 3 2 4s-1.5 1.5-1 2.5 2 2.5 3 3 1.5-1 2.5-1 4 1 4 2-1 3-3 3C6 15 1 10 1 4c0-2 2-3 3-3z"/></svg>
        1-800-555-4926
      </li>
      <li>
        <svg viewBox="0 0 16 16"><rect x="4" y="1" width="8" height="14" rx="1.5" fill="none" stroke="#f47b20" stroke-width="1.6"/><circle cx="8" cy="12.5" r="0.9" fill="#f47b20"/></svg>
        222-555-7312
      </li>
      <li>
        <svg viewBox="0 0 16 16"><rect x="1" y="3" width="14" height="10" fill="#f47b20"/><path d="M1 3l7 6 7-6" fill="none" stroke="#fff" stroke-width="1.3"/></svg>
        dale@buildlinkage.com
      </li>
    </ul>

    <div class="address">
      PO Box 874 Brockridge,<br>NR S0M2T7
    </div>

    <div class="footer-band">
      <div class="footer-band__slate"></div>
      <div class="footer-band__accent">www.buildlinkage.com</div>
    </div>
  </section>
</main>
</body>
</html>
```